Bluestone Nine LLC Flyer Design

Marketing Materials for Real Estate Company. This flyer will be used to promote the company throughout the Commercial Real Estate business in the United States. The team has been together for 15 years. We are the middle guys between the Tenant, Broker, and the Owner. In the case of working with a Franchisor, we will be their Plug and Play leasing arm that will assist their new Franchisee's with their site selection, lease negotiations, design and construction management.

Target Market(s)

Real Estate Owners, Franchisor's, and Brokers

Font styles to use
Serif

Colors

Designer to choose colors to be used in the design.

Requirements
Must have
• The flyer must have......
• 1. The Best Leasing Machine On The Planet
• 2. Over the past 15 years our group has completed 4,492 lease transactions resulting in leasing 17,803,114 square feet in shopping centers across the United States.
• 3. Plug and Play Leasing Specialists. We handle the details between when the broker shows up with the space and the tenant and completing the lease negotiations, legal negotiations and documentation, and construction management to Certificate of Occupancy.
• 4. For Information Call Colette Varga at 555-014-2763 or Wendy Falk at 555-017-8302.
Nice to have
• National Tenants the we have completed transactions with....
• Pellmart, Fresh Basket, Harbor Pams, Vexo, Dunn, QV Rendo, Burrasco, Pattersons, Wrap Shack, Brewhorns, Summit Workout, ShipVo, Tredwell, PKN, Halvorsons, Q&L, Ledger Union Bank, Hen Haus-O, Lotus Kitchen, Furvo, Dex-Mart, Fieldly, and Orbit Theaters

```html
<!DOCTYPE html>
<html lang="en">
<head>
<meta charset="utf-8">
<title>Bluestone Nine LLC – Leasing Flyer</title>
<link rel="stylesheet" href="https://fonts.googleapis.com/css2?family=Montserrat:wght@500;600;700;800&display=swap">
<style>
  :root {
    --backdrop: #d8d9d5;
    --ink-dark: #2a2d2c;
    --ink-deeper: #1f2221;
    --leaf: #8dc63f;
    --leaf-deep: #3f8a3a;
    --leaf-soft: #b9de7a;
    --paper: #e6eeee;
    --sky: #7fa8ad;
    --sky-deep: #2f5f66;
    --placeholder: #a7a9ac;
    --white: #ffffff;
    --text-dark: #1b1d1c;
  }
  html, body {
    margin: 0;
    padding: 0;
    width: 1120px;
    height: 1200px;
    overflow: hidden;
    background: var(--backdrop);
  }
  .flyer {
    position: absolute;
    left: 150px;
    top: 20px;
    width: 820px;
    height: 1160px;
    box-shadow: 0 6px 24px rgba(0,0,0,0.25);
  }
  .flyer svg { display: block; }
  .headline { font-family: 'Montserrat', sans-serif; }
  .headline-small { font-size: 50px; font-weight: 700; }
  .headline-large { font-size: 88px; font-weight: 800; letter-spacing: -1px; }
  .headline-planet { font-size: 50px; font-weight: 700; }
  .quote-text { font-family: 'Montserrat', sans-serif; font-size: 19.5px; font-weight: 500; fill: var(--text-dark); }
  .quote-mark { font-family: 'Montserrat', sans-serif; font-size: 120px; font-weight: 800; fill: var(--leaf-deep); opacity: 0.55; }
  .contact-name { font-family: 'Montserrat', sans-serif; font-size: 25px; font-weight: 800; fill: var(--text-dark); }
  .contact-phone { font-family: 'Montserrat', sans-serif; font-size: 21px; font-weight: 700; fill: var(--text-dark); }
  .service-text { font-family: 'Montserrat', sans-serif; font-size: 17.5px; font-weight: 500; fill: var(--white); }
  .website { font-family: 'Montserrat', sans-serif; font-size: 25px; font-weight: 600; fill: var(--leaf); }
</style>
</head>
<body>
<div class="flyer">
  <svg width="820" height="1160" viewBox="0 0 820 1160" xmlns="http://www.w3.org/2000/svg">
    <defs>
      <linearGradient id="skyline-tone" x1="0" y1="0" x2="0.4" y2="1">
        <stop offset="0" stop-color="#a9c8c8"/>
        <stop offset="0.55" stop-color="var(--sky)"/>
        <stop offset="1" stop-color="var(--sky-deep)"/>
      </linearGradient>
      <linearGradient id="band-green" x1="1" y1="0" x2="0" y2="1">
        <stop offset="0" stop-color="var(--leaf-soft)"/>
        <stop offset="0.45" stop-color="var(--leaf)"/>
        <stop offset="1" stop-color="var(--leaf-deep)"/>
      </linearGradient>
      <linearGradient id="paper-tone" x1="0" y1="0" x2="1" y2="1">
        <stop offset="0" stop-color="#f2f6f5"/>
        <stop offset="1" stop-color="#d5e2e2"/>
      </linearGradient>
    </defs>

    <!-- base -->
    <rect class="flyer-base" width="820" height="1160" fill="var(--ink-dark)"/>

    <!-- city skyline photo area -->
    <polygon class="skyline-photo" role="img" aria-label="Photo of a city skyline with tall office towers by the water"
             points="0,0 190,0 580,458 120,610 0,455" fill="url(#skyline-tone)"/>

    <!-- left accent stripe and dark wedge -->
    <polygon class="accent-stripe" points="0,455 120,610 108,614 0,478" fill="var(--white)" opacity="0.85"/>
    <polygon class="dark-wedge" points="0,478 108,614 0,642" fill="var(--ink-deeper)"/>

    <!-- main green band -->
    <polygon class="green-band" points="820,382 820,720 365,862 0,977 0,642" fill="url(#band-green)"/>
    <polygon class="green-band-sheen" points="820,382 0,642 0,700 600,560" fill="var(--white)" opacity="0.08"/>

    <!-- pale lower-left panel -->
    <polygon class="paper-panel" points="0,977 365,862 640,1160 0,1160" fill="url(#paper-tone)"/>

    <!-- dark lower-right panel -->
    <polygon class="service-panel" points="820,720 820,1160 640,1160 365,862" fill="var(--ink-deeper)"/>

    <!-- headline -->
    <g class="headline" text-anchor="end">
      <text class="headline-small" x="777" y="117" fill="var(--white)">The Best</text>
      <text class="headline-large" x="777" y="204" fill="var(--leaf)">LEASING</text>
      <text class="headline-large" x="772" y="292" fill="var(--white)">MACHINE</text>
      <text class="headline-planet" x="772" y="354" fill="var(--leaf)">On The Planet</text>
    </g>

    <!-- testimonial quote -->
    <text class="quote-mark" x="450" y="596">“</text>
    <text class="quote-mark" x="710" y="760">”</text>
    <g text-anchor="end">
      <text class="quote-text" x="768" y="554">Over the past 15 years</text>
      <text class="quote-text" x="768" y="580">our group has completed 4,492</text>
      <text class="quote-text" x="768" y="606">lease transactions resulting in leasing</text>
      <text class="quote-text" x="768" y="632">17,803,114 square feet in shopping</text>
      <text class="quote-text" x="768" y="658">centers across the United States.</text>
    </g>

    <!-- contacts -->
    <g class="contact">
      <line x1="190" y1="809" x2="390" y2="809" stroke="var(--text-dark)" stroke-width="1.5"/>
      <circle cx="390" cy="809" r="4.5" fill="var(--text-dark)"/>
      <circle class="contact-photo" role="img" aria-label="Portrait of Colette Varga" cx="117" cy="757" r="80" fill="var(--placeholder)" stroke="var(--ink-deeper)" stroke-width="5"/>
      <text class="contact-name" x="210" y="772">Colette Varga</text>
      <text class="contact-phone" x="210" y="797">555-014-2763</text>
    </g>
    <g class="contact">
      <line x1="183" y1="1006" x2="378" y2="1006" stroke="var(--text-dark)" stroke-width="1.5"/>
      <circle cx="378" cy="1006" r="4.5" fill="var(--text-dark)"/>
      <circle class="contact-photo" role="img" aria-label="Portrait of Wendy Falk" cx="110" cy="955" r="80" fill="var(--placeholder)" stroke="var(--ink-deeper)" stroke-width="5"/>
      <text class="contact-name" x="210" y="969">Wendy Falk</text>
      <text class="contact-phone" x="210" y="994">555-017-8302</text>
    </g>

    <!-- website -->
    <rect class="website-rule" x="25" y="1070" width="453" height="7" fill="var(--leaf)"/>
    <text class="website" x="23" y="1112">www.bluestoneninellc.com</text>

    <!-- services -->
    <g text-anchor="end">
      <text class="service-text" x="788" y="866">Plug and Play Leasing</text>
      <text class="service-text" x="788" y="887">Specialists. We handle the</text>
      <text class="service-text" x="788" y="909">details between when the broker</text>
      <text class="service-text" x="788" y="930">shows up with the space and the</text>
      <text class="service-text" x="788" y="952">tenant and completing the</text>
      <text class="service-text" x="788" y="973">lease negotiations, legal</text>
      <text class="service-text" x="788" y="995">negotiations and</text>
      <text class="service-text" x="788" y="1016">documentation, and</text>
      <text class="service-text" x="788" y="1038">construction</text>
      <text class="service-text" x="788" y="1059">management to</text>
      <text class="service-text" x="788" y="1081">Certificate of</text>
      <text class="service-text" x="788" y="1102">Occupancy.</text>
    </g>
  </svg>
</div>
</body>
</html>
```